Zorpax.com (Dedicated servers Provider)

We provide dedicated servers for clients around the world. We have created a layout for you. You need to create exactly the design based on these sketches. All text, you can take from our sketches (later we will replace them).

Target Market(s)

Web site owners and web developers

Requirements
Should not have
• The design should not use old-style fonts.

```html
<!DOCTYPE html>
<html lang="en">
<head>
<meta charset="utf-8">
<title>Zorpax Servers – Dedicated Servers</title>
<link rel="stylesheet" href="https://fonts.googleapis.com/css2?family=Arimo:wght@400;700&display=swap">
<style>
:root{
  --page:#ebebeb;
  --dark:#1b1b1b;
  --darker:#0e0e0e;
  --footer:#262626;
  --green:#9cc625;
  --green-dark:#77a40c;
  --green-text:#8db41d;
  --red:#d20f0f;
  --red-dark:#a80000;
  --blue:#2b8bd6;
  --orange:#f1a21e;
  --text:#333;
  --muted:#8a8a8a;
  --line:#dedede;
  --white:#fff;
}
*{box-sizing:border-box;margin:0;padding:0}
html,body{width:1200px;height:2191px;overflow:hidden}
body{background:var(--page);font-family:"Arimo",Arial,sans-serif;color:var(--text);position:relative}
a{color:inherit;text-decoration:none}

/* header */
.topbar{position:absolute;left:0;top:0;width:1200px;height:22px;background:var(--darker)}
.topbar-links{position:absolute;left:712px;top:4px;font-size:11px;color:#777;display:flex;gap:14px}
.header{position:absolute;left:0;top:22px;width:1200px;height:107px;background:linear-gradient(#2c2c2c,#1e1e1e)}
.logo{position:absolute;left:132px;top:50px;display:flex;align-items:center;gap:10px;color:var(--white);font-size:40px;font-weight:700;letter-spacing:-1px}
.logo-mark{width:34px;height:34px;background:var(--green)}
.chat-box{position:absolute;left:926px;top:-22px;width:142px;height:65px;background:#000;border-radius:0 0 4px 4px;color:#ddd;font-size:11px;padding:5px 10px}
.chat-box .bubble{display:inline-block;width:16px;height:12px;background:#3aa3e3;border-radius:6px;vertical-align:middle;margin-right:6px}
.follow{display:flex;align-items:center;gap:5px;margin-top:10px}
.follow span.sq{width:20px;height:20px;border-radius:2px}
.callout{position:absolute;right:140px;top:62px;font-size:15px;font-weight:700;color:var(--white);display:flex;align-items:center;gap:8px}
.callout .q{color:var(--orange);font-weight:400}
.callout .num{color:var(--orange)}
.callout .ico{width:18px;height:14px;background:var(--orange);border-radius:3px}

/* nav */
.navbar{position:absolute;left:0;top:129px;width:1200px;height:39px;background:linear-gradient(#b3d83a,var(--green-dark));border-bottom:1px solid #5f8a05}
.nav{position:absolute;left:132px;top:0;display:flex;height:39px}
.nav a{display:flex;align-items:center;justify-content:center;color:var(--white);font-weight:700;font-size:15px;text-transform:uppercase;border-right:1px solid rgba(255,255,255,.25)}
.nav a.active{background:#111}

/* slider */
.slider{position:absolute;left:132px;top:199px;width:936px;height:329px;background:linear-gradient(135deg,#303030,#121212);overflow:hidden;box-shadow:0 12px 14px -10px rgba(0,0,0,.35)}
.slider-title{position:absolute;left:91px;top:20px;font-size:42px;color:var(--white);letter-spacing:.5px}
.slider-sub{position:absolute;left:395px;top:66px;font-size:10px;color:#aaa}
.slide-photo{position:absolute;left:0;top:0}
.server-img{position:absolute;left:70px;top:115px;width:150px;height:123px;background:linear-gradient(#3a3a3a,#151515);border:1px solid #444}
.checks{position:absolute;left:250px;top:112px;list-style:none;color:var(--white);font-size:12.5px}
.checks li{height:28.5px;display:flex;align-items:center;gap:10px}
.checks li::before{content:"";width:13px;height:13px;background:var(--green);border-radius:2px;flex:none;box-shadow:inset 0 0 0 2px #567d00}
.btn-order-big{position:absolute;left:252px;top:255px;width:168px;height:43px;background:linear-gradient(#f02020,var(--red-dark));border-radius:4px;color:var(--white);font-weight:700;font-size:18px;display:flex;align-items:center;justify-content:center;box-shadow:0 0 0 3px #111}
.slide-arrow{position:absolute;top:338px;width:43px;height:46px;background:linear-gradient(#b4da3c,var(--green-dark));border-radius:3px}
.slide-arrow svg{position:absolute;left:14px;top:15px}

/* plans */
.tabs{position:absolute;left:132px;top:571px;display:flex;height:40px}
.tab{height:40px;display:flex;align-items:center;justify-content:center;font-size:15px;color:#999;background:#f3f3f3;border:1px solid #d4d4d4;border-bottom:none;border-radius:4px 4px 0 0}
.tab.active{background:var(--white);color:#333;z-index:2}
.plans{position:absolute;left:132px;top:610px;width:936px;height:556px;background:var(--white);border:1px solid #d4d4d4}
.card{position:absolute;top:20px;width:250px;height:288px;background:var(--white);box-shadow:0 0 8px rgba(0,0,0,.2)}
.card.featured{background:#f4f8e4}
.card-label{position:absolute;left:50%;transform:translateX(-50%);top:3px;height:29px;background:#1e1e1e;color:var(--white);font-weight:700;font-size:15px;display:flex;align-items:center;justify-content:center;clip-path:polygon(0 0,100% 0,92% 100%,8% 100%);padding:0 26px;white-space:nowrap}
.card-img{position:absolute;left:55px;top:48px;width:160px;height:58px;background:linear-gradient(#dadada,#9a9a9a);border:1px solid #888}
.card-from{position:absolute;left:62px;top:124px;font-size:10px;color:#444}
.price{position:absolute;left:14px;top:140px;font-size:44px;font-weight:700;color:#222;letter-spacing:-1px;width:130px;height:50px}
.price sup{font-size:20px;vertical-align:top;position:relative;top:6px}
.price .cents{font-size:18px;vertical-align:top;position:relative;top:5px}
.price .per{font-size:8px;position:absolute;left:104px;top:30px;font-weight:400;letter-spacing:0;line-height:8px;width:20px}
.specs{position:absolute;left:149px;top:124px;font-size:11px;color:#333;line-height:22px;list-style:none}
.term{position:absolute;left:149px;top:190px;width:90px;height:18px;border:1px solid #bbb;font-size:9px;display:flex;align-items:center;padding-left:5px;background:var(--white);white-space:nowrap}
.term::after{content:"";position:absolute;right:-1px;top:-1px;width:14px;height:18px;background:#333}
.all-link{position:absolute;left:38px;top:222px;font-size:10px;color:#444;border-bottom:1px solid #444}
.btn-order{position:absolute;left:154px;top:217px;width:81px;height:26px;background:linear-gradient(#ee1d1d,var(--red-dark));color:var(--white);font-weight:700;font-size:12px;border-radius:3px;display:flex;align-items:center;justify-content:center}
.divider{position:absolute;left:20px;top:328px;width:894px;height:1px;background:var(--line)}
.map{position:absolute;left:30px;top:366px;width:180px;height:112px;background:radial-gradient(ellipse at 40% 40%,#7fd0ea,#3b98c4 70%,transparent 72%),#d9d9d9;border-radius:40% 45% 30% 40%}
.map-caption{position:absolute;left:44px;top:492px;font-size:9px;color:#555}
.badges{position:absolute;list-style:none}
.badges li{height:30px;margin-bottom:7px;border-radius:15px;background:linear-gradient(#fff,#ececec);box-shadow:0 1px 3px rgba(0,0,0,.3);display:flex;align-items:center;gap:8px;font-size:13px;font-weight:700;color:#222;padding-left:3px}
.badges .dot{width:24px;height:24px;border-radius:50%;background:var(--red);display:flex;align-items:center;justify-content:center;flex:none}

/* testimonial */
.testimonial{position:absolute;left:132px;top:1176px;width:936px;height:206px;background:#dcdcdc}
.quote{position:absolute;left:150px;top:40px;width:636px;text-align:center;text-transform:uppercase;font-size:17px;line-height:24px;color:#7a7a7a}
.quote-author{position:absolute;left:0;width:936px;top:158px;text-align:center;font-size:12px;color:#888}
.qmark{position:absolute;font-size:110px;color:#bdbdbd;font-weight:700;line-height:1}

/* partners */
.partners{position:absolute;left:132px;top:1397px;width:936px;height:105px;background:#232323}
.partners .arr{position:absolute;top:42px}
.partner{position:absolute;top:40px;height:24px;background:#cfcfcf;border-radius:3px}
.award{position:absolute;left:683px;top:36px;color:var(--white);font-weight:700;font-size:11px;line-height:12px;text-align:right}
.award small{display:block;color:var(--blue);font-weight:400;font-size:9px}
.award-seal{position:absolute;left:825px;top:30px;width:52px;height:52px;border-radius:50%;background:#d8d8d8;border:3px solid #fff}

/* benefits */
.benefits{position:absolute;left:132px;top:1515px;width:936px;height:417px;background:var(--white)}
.benefits h2{position:absolute;font-size:17px;color:var(--green-text);font-weight:700}
.rule{position:absolute;height:1px;background:var(--line)}
.benefit{position:absolute;left:26px;width:600px;height:56px}
.benefit .ico{position:absolute;left:0;top:0;width:51px;height:51px;background:#555;border:3px solid #ddd;display:flex;align-items:center;justify-content:center}
.benefit h3{position:absolute;left:60px;top:0;font-size:13px;color:var(--red);font-weight:400}
.benefit p{position:absolute;left:60px;top:19px;font-size:10px;line-height:13px;color:#999;width:480px}
.stat{position:absolute;left:665px;width:250px;height:44px}
.stat .play{position:absolute;left:0;top:0;width:40px;height:40px;background:#4a4a4a;display:flex;align-items:center;justify-content:center}
.stat b{position:absolute;left:51px;top:0;font-size:17px;color:var(--blue);font-weight:400}
.stat p{position:absolute;left:51px;top:22px;font-size:9.5px;line-height:12px;color:#999;width:190px}

/* footer */
.footer{position:absolute;left:0;top:1932px;width:1200px;height:259px;background:radial-gradient(ellipse at 50% 0,#3a3a3a,var(--footer) 60%)}
.footer h4{position:absolute;color:var(--white);font-size:13px;font-weight:700}
.footer .keep{font-size:20px}
.f-text{position:absolute;color:#999;font-size:12px;line-height:16px}
.f-link{color:var(--blue)}
.f-links{position:absolute;list-style:none;font-size:10px;color:var(--blue);line-height:18px}
.vline{position:absolute;top:20px;width:1px;height:190px;background:#444}
.social-btn{position:absolute;height:18px;background:#e9e9e9;border:1px solid #999;border-radius:2px;font-size:10px;color:#333;display:flex;align-items:center;padding:0 6px;gap:4px}
.social-btn i{width:10px;height:10px;background:#3a6dc0;display:inline-block}
.bottom-line{position:absolute;left:154px;top:211px;width:892px;height:1px;background:#3d3d3d}
.copy{position:absolute;left:456px;top:228px;font-size:10px;color:#888}
</style>
</head>
<body>

<div class="topbar">
  <div class="topbar-links"><a href="#">User Registration</a><span>|</span><a href="#">Customer Login</a></div>
</div>
<header class="header">
  <a class="logo" href="#"><span class="logo-mark"></span>Zorpax</a>
  <div class="chat-box">
    <div><span class="bubble"></span>Live Chat Online</div>
    <div class="follow">Follow us <span class="sq" style="background:#3b5a9a"></span><span class="sq" style="background:#2ba8e0"></span><span class="sq" style="background:#1a78b4"></span></div>
  </div>
  <div class="callout"><span class="ico"></span><span class="q">Questions?</span> Call Now! <span class="num">0.800.555.0199</span></div>
</header>

<nav class="navbar">
  <div class="nav">
    <a class="active" href="#" style="width:94px">Home</a>
    <a href="#" style="width:148px">Domains</a>
    <a href="#" style="width:178px">Web Hosting</a>
    <a href="#" style="width:185px">Latest News</a>
    <a href="#" style="width:172px">My Account</a>
    <a href="#" style="width:159px;border-right:none">Contact</a>
  </div>
</nav>

<section class="slider">
  <svg class="slide-photo" width="936" height="329" role="img" aria-label="Photo of a smiling office team giving a thumbs up">
    <defs><linearGradient id="photoTone" x1="0" y1="0" x2="1" y2="1"><stop offset="0" stop-color="#c9c2b6"/><stop offset=".5" stop-color="#e8e4dc"/><stop offset="1" stop-color="#8d8478"/></linearGradient></defs>
    <polygon points="560,0 936,0 936,329 450,329" fill="url(#photoTone)"/>
  </svg>
  <div class="slider-title">DEDICATED SERVERS</div>
  <div class="slider-sub">FROM NORTHLANE</div>
  <div class="server-img" role="img" aria-label="Rack server illustration"></div>
  <ul class="checks">
    <li>Self-owned data centre</li>
    <li>24 x 7 x 365 on-site support</li>
    <li>100% uptime guarantee</li>
    <li>Industry leading control panel</li>
    <li>Custom servers; 24 setup</li>
  </ul>
  <a class="btn-order-big" href="#">ORDER NOW</a>
</section>
<a class="slide-arrow" href="#" style="left:123px"><svg width="14" height="16"><polygon points="12,1 2,8 12,15" fill="#fff"/></svg></a>
<a class="slide-arrow" href="#" style="left:1032px"><svg width="14" height="16"><polygon points="2,1 12,8 2,15" fill="#fff"/></svg></a>

<div class="tabs">
  <div class="tab active" style="width:176px">Dedicated Servers</div>
  <div class="tab" style="width:241px">Web Hosting</div>
  <div class="tab" style="width:257px">Virtual Private Servers</div>
</div>
<section class="plans">
  <article class="card" style="left:19px">
    <div class="card-label">Vantor 4 2.4GHz</div>
    <div class="card-img" role="img" aria-label="Server unit"></div>
    <div class="card-from">Plans starting at</div>
    <div class="price"><sup>$</sup>309<span class="cents">00</span><span class="per">per mo.</span></div>
    <ul class="specs"><li>80GB SATA HD</li><li>1GB RAM</li><li>1TB Bandwidth</li></ul>
    <div class="term">1 year - 39.00/mo</div>
    <a class="all-link" href="#">All Dedicated Servers</a>
    <a class="btn-order" href="#">ORDER</a>
  </article>
  <article class="card featured" style="left:326px">
    <div class="card-label">Cirra C7 2.66-2.93Ghz</div>
    <div class="card-img" role="img" aria-label="Server unit"></div>
    <div class="card-from">Plans starting at</div>
    <div class="price"><sup>$</sup>219<span class="cents">00</span><span class="per">per mo.</span></div>
    <ul class="specs"><li>80GB SATA HD</li><li>1GB RAM</li><li>1TB Bandwidth</li></ul>
    <div class="term">1 year - 39.00/mo</div>
    <a class="all-link" href="#">All Dedicated Servers</a>
    <a class="btn-order" href="#">ORDER</a>
  </article>
  <article class="card" style="left:634px">
    <div class="card-label">Dual Helix H8-4410</div>
    <div class="card-img" role="img" aria-label="Server unit"></div>
    <div class="card-from">Plans starting at</div>
    <div class="price"><sup>$</sup>395<span class="cents">00</span><span class="per">per mo.</span></div>
    <ul class="specs"><li>1000 SATA HD</li><li>8GB RAM</li><li>10TB Bandwidth</li></ul>
    <div class="term">1 year - 39.00/mo</div>
    <a class="all-link" href="#">All Dedicated Servers</a>
    <a class="btn-order" href="#">ORDER</a>
  </article>
  <div class="divider"></div>
  <div class="map" role="img" aria-label="Map of the United States with network links"></div>
  <div class="map-caption">Now offering Hostwell Panel 11</div>
  <ul class="badges" style="left:317px;top:386px;width:242px">
    <li><span class="dot"><svg width="12" height="10"><polyline points="1,5 4.5,8.5 11,1.5" fill="none" stroke="#fff" stroke-width="2.2"/></svg></span>100% Network Uptime SLA</li>
    <li><span class="dot"><svg width="12" height="10"><polyline points="1,5 4.5,8.5 11,1.5" fill="none" stroke="#fff" stroke-width="2.2"/></svg></span>ISO 9001:2008 Certified</li>
    <li><span class="dot"><svg width="12" height="10"><polyline points="1,5 4.5,8.5 11,1.5" fill="none" stroke="#fff" stroke-width="2.2"/></svg></span>24/7 ITIL Technical Support</li>
  </ul>
  <ul class="badges" style="left:644px;top:386px;width:270px">
    <li><span class="dot"><svg width="12" height="10"><polyline points="1,5 4.5,8.5 11,1.5" fill="none" stroke="#fff" stroke-width="2.2"/></svg></span>3 SSAE-16 Certified Date Centers</li>
    <li><span class="dot"><svg width="12" height="10"><polyline points="1,5 4.5,8.5 11,1.5" fill="none" stroke="#fff" stroke-width="2.2"/></svg></span>Coast-to-Coast IP Backbone</li>
    <li><span class="dot"><svg width="12" height="10"><polyline points="1,5 4.5,8.5 11,1.5" fill="none" stroke="#fff" stroke-width="2.2"/></svg></span>Award Winning Since 1996</li>
  </ul>
</section>

<section class="testimonial">
  <span class="qmark" style="left:118px;top:14px">“</span>
  <p class="quote">We had simply dummy text of the printing and typesetting industry. Lorem Ipsum has been the industry's standard dummy text ever since the 1500s, when an unknown printer took a galley of type and scrambled it to make a type specimen book.</p>
  <span class="qmark" style="left:792px;top:104px">”</span>
  <div class="quote-author">Mara Quill quillpost.com</div>
</section>

<section class="partners">
  <svg class="arr" style="left:20px" width="12" height="20"><polyline points="10,2 3,10 10,18" fill="none" stroke="#fff" stroke-width="3"/></svg>
  <div class="partner" style="left:70px;width:32px;border-radius:50%;height:32px;top:36px"></div>
  <div class="partner" style="left:116px;width:66px"></div>
  <div class="partner" style="left:196px;width:68px"></div>
  <div class="partner" style="left:276px;width:66px"></div>
  <div class="partner" style="left:358px;width:20px;border-radius:50%;height:20px;top:42px"></div>
  <div class="partner" style="left:394px;width:72px"></div>
  <div class="partner" style="left:480px;width:46px;border-radius:50%;height:28px;top:38px"></div>
  <div class="partner" style="left:544px;width:68px"></div>
  <div class="award">AWARD WINNING<br>DEDICATED HOSTING<small>View Our Awards</small></div>
  <div class="award-seal"></div>
  <svg class="arr" style="left:904px" width="12" height="20"><polyline points="2,2 9,10 2,18" fill="none" stroke="#fff" stroke-width="3"/></svg>
</section>

<section class="benefits">
  <h2 style="left:22px;top:36px">SwiftRack - The Smart Choice For Dedicated Services</h2>
  <div class="rule" style="left:22px;top:72px;width:590px"></div>
  <div class="benefit" style="top:94px">
    <div class="ico"><svg width="20" height="22"><rect x="2" y="1" width="16" height="20" fill="none" stroke="#fff" stroke-width="2"/><circle cx="10" cy="9" r="3" fill="#fff"/></svg></div>
    <h3>Business-Class Brightline Hardware</h3>
    <p>Contrary to popular belief, Lorem Ipsum is not simply random text. It has roots in a piece of classical Latin literature from 45 BC, making it over 2000 years old.</p>
  </div>
  <div class="rule" style="left:22px;top:155px;width:590px"></div>
  <div class="benefit" style="top:162px">
    <div class="ico"><svg width="22" height="22"><circle cx="11" cy="11" r="9" fill="none" stroke="#fff" stroke-width="2"/><path d="M5 8 Q11 12 9 18 M12 3 Q15 9 19 11" stroke="#fff" stroke-width="2" fill="none"/></svg></div>
    <h3>99.9% Uptime SLA</h3>
    <p>Contrary to popular belief, Lorem Ipsum is not simply random text. It has roots in a piece of classical Latin literature from 45 BC, making it over 2000 years old.</p>
  </div>
  <div class="rule" style="left:22px;top:223px;width:590px"></div>
  <div class="benefit" style="top:231px">
    <div class="ico"><svg width="22" height="20"><path d="M2 2 H20 V14 H9 L4 18 V14 H2 Z" fill="#fff"/></svg></div>
    <h3>24/7/365 Expert UK Technical Support</h3>
    <p>Contrary to popular belief, Lorem Ipsum is not simply random text. It has roots in a piece of classical Latin literature from 45 BC, making it over 2000 years old.</p>
  </div>
  <div class="rule" style="left:22px;top:292px;width:590px"></div>
  <div class="benefit" style="top:300px">
    <div class="ico"><svg width="22" height="22"><circle cx="11" cy="11" r="7" fill="none" stroke="#fff" stroke-width="4" stroke-dasharray="3 2.5"/><circle cx="11" cy="11" r="3" fill="#fff"/></svg></div>
    <h3>Fast Setup</h3>
    <p>Contrary to popular belief, Lorem Ipsum is not simply random text. It has roots in a piece of classical Latin literature from 45 BC, making it over 2000 years old.</p>
  </div>

  <h2 style="left:665px;top:40px">SwiftRack</h2>
  <div class="rule" style="left:665px;top:72px;width:250px"></div>
  <div class="stat" style="top:98px"><div class="play"><svg width="10" height="12"><polygon points="1,1 9,6 1,11" fill="#fff"/></svg></div><b>1,800,000</b><p>The standard chunk of Lorem Ipsum used since the below those interested.</p></div>
  <div class="rule" style="left:665px;top:148px;width:250px"></div>
  <div class="stat" style="top:161px"><div class="play"><svg width="10" height="12"><polygon points="1,1 9,6 1,11" fill="#fff"/></svg></div><b>40,000</b><p>The standard chunk of Lorem Ipsum used since the below those interested.</p></div>
  <div class="rule" style="left:665px;top:216px;width:250px"></div>
  <div class="stat" style="top:233px"><div class="play"><svg width="10" height="12"><polygon points="1,1 9,6 1,11" fill="#fff"/></svg></div><b>500,000</b><p>The standard chunk of Lorem Ipsum used since the below those interested.</p></div>
  <div class="rule" style="left:665px;top:294px;width:250px"></div>
  <div class="stat" style="top:312px"><div class="play"><svg width="10" height="12"><polygon points="1,1 9,6 1,11" fill="#fff"/></svg></div><b>490,000</b><p>The standard chunk of Lorem Ipsum used since the below those interested.</p></div>
</section>

<footer class="footer">
  <h4 class="keep" style="left:154px;top:30px">Keep it simple!</h4>
  <p class="f-text" style="left:154px;top:66px;width:240px;font-size:13px">The web changes people and the things they do. This is way we develop incresingly reliable, easy-to-use and intutice sevice</p>
  <a class="f-text f-link" href="#" style="left:154px;top:143px;font-size:11px;font-weight:700">Learn more about SwiftRack</a>

  <div class="vline" style="left:420px"></div>
  <h4 style="left:451px;top:30px">About SwiftRack Servers</h4>
  <ul class="f-links" style="left:451px;top:63px"><li>About Us</li><li>Contact Us</li><li>Terms &amp; Conditions</li></ul>
  <ul class="f-links" style="left:573px;top:63px"><li>Support</li><li>Why Choose Us</li><li>Service Level Agreement</li></ul>
  <p class="f-text" style="left:451px;top:129px;font-size:10px;color:#aaa">Copyright © Kestrel Ltd 2012 . All rights reserved</p>
  <p class="f-text" style="left:451px;top:162px;width:290px;font-size:10px;line-height:14px;color:#aaa">SwiftRack Servers is part of the <span class="f-link">Orbis Group</span>. Read more on the Orbis <span class="f-link">Blog</span></p>

  <div class="vline" style="left:756px"></div>
  <h4 style="left:771px;top:30px;font-size:12px">Information</h4>
  <p class="f-text" style="left:771px;top:62px;width:270px;font-size:10px;line-height:13px;color:#aaa">Contact us via our Support Ticket System in you <span class="f-link">Online Control Panel</span> or alternatively call us on the number below:</p>
  <p class="f-text" style="left:771px;top:106px;font-size:20px;color:#999;font-weight:700">+44 (0)1632 960 418</p>
  <div class="social-btn" style="left:771px;top:148px"><i></i>Like <b>25</b></div>
  <div class="social-btn" style="left:846px;top:148px"><i style="background:#2ba8e0"></i>Follow @swiftrack</div>
  <div class="social-btn" style="left:771px;top:172px;background:#d44;color:#fff;border-color:#b33">+1</div>
  <p class="f-text" style="left:805px;top:173px;font-size:10px;color:#aaa">+44 &nbsp;Recommend this</p>

  <div class="bottom-line"></div>
  <p class="copy">Copyright © 2012 Zorpax Servers</p>
</footer>

</body>
</html>
```